Business card design needed

Hi.
We need a business card for a building and construction business which specialises in all aspects of domestic building. This includes new and existing works, insurance and shop front works.
We would like to see designs similar to the pic attached.the idea that we are having is a universal card that can be used on shirts,the side of a ute and trailer,fridge magnets this like this, this card will need to be easy to read from advertising point of veiw ie ( ute in transit) a mixer of Blue's would be the main colours for any logo's or graphics and light colours or even white as the back ground choice as we want to stand out against white car. and easy to read while traveling please find some samples of what we like

Target Market(s)

other builders, home owners, insurance builders, anyone who may need work done to their properties home or business

Industry/Entity Type

Construction

Contact Information for Business Card

Company name: Colin Dartmoor Constructions
Name: Colin Dartmoor
Mobile: 0461735920
Address: POBox 728 Werribee
Email: colindartmoor@maildrop-example.com.au

Requirements
Must have
• Must have:
Name: Colin Dartmoor
Mobile: 0461735920
ABN: 47 803 516 229
The background needs to be able to be put onto car doors and onto tshirts.
Nice to have
• could have a slogan like "the person to bring ur dreams to reality" "done right the first time" "for allMatainace and construction needs" doesnt have to be one of those but something like that
Should not have
• nothing like clip art or basic font

```html
<!DOCTYPE html>
<html lang="en">
<head>
<meta charset="utf-8">
<title>Colin Dartmoor Constructions – Business Card</title>
<link rel="stylesheet" href="https://fonts.googleapis.com/css2?family=PT+Serif:wght@400;700&display=swap">
<style>
  :root {
    --page-bg: #e4e6e8;
    --card-white: #f7f7f7;
    --ink: #1b1b1b;
    --brand-dark: #0b5f80;
    --brand-blue: #1aa3d1;
    --brand-light: #3cc0ea;
    --back-deep: #004a6e;
    --back-mid: #0a86b4;
    --back-glow: #22b4e2;
    --white: #ffffff;
  }
  * { margin: 0; padding: 0; box-sizing: border-box; }
  html, body {
    width: 1200px; height: 900px; overflow: hidden;
    background: var(--page-bg);
    font-family: "PT Serif", Georgia, serif;
  }
  .canvas { position: relative; width: 1200px; height: 900px; }

  .card {
    position: absolute; left: 290px; width: 620px; height: 355px;
    box-shadow: 0 6px 18px rgba(0,0,0,0.18);
    overflow: hidden;
  }
  .card-front { top: 50px; background: var(--card-white); color: var(--ink); }
  .card-back {
    top: 490px;
    background: radial-gradient(ellipse at 50% 35%, var(--back-glow) 0%, var(--back-mid) 40%, var(--back-deep) 100%);
  }

  /* Front */
  .brand-row { position: absolute; left: 30px; top: 24px; display: flex; align-items: center; gap: 20px; }
  .brand-dot {
    width: 92px; height: 92px; border-radius: 50%;
    background: radial-gradient(circle at 40% 60%, var(--brand-light), var(--brand-dark));
  }
  .brand-name { font-weight: 700; font-size: 31px; line-height: 1.1; color: var(--brand-dark); }

  .services { position: absolute; top: 138px; left: 200px; display: flex; gap: 40px; }
  .services ul { list-style: none; }
  .services li { font-size: 15px; line-height: 1.35; }
  .services li::before { content: "•"; color: var(--brand-blue); margin-right: 6px; }

  .contact { position: absolute; left: 30px; top: 192px; }
  .person-name { font-size: 31px; color: var(--brand-blue); margin-bottom: 4px; font-weight: 400; line-height: 1.2; }
  .contact-line { font-size: 17px; line-height: 1.35; }
  .label { color: var(--brand-blue); margin-right: 4px; }

  .business-info { position: absolute; left: 390px; top: 296px; font-size: 17px; line-height: 1.4; }

  /* Back */
  .back-mark { position: absolute; inset: 0; display: flex; flex-direction: column; align-items: center; justify-content: center; gap: 16px; }
  .back-dot { width: 118px; height: 118px; border-radius: 50%; background: var(--white); }
  .back-name { font-weight: 700; font-size: 42px; color: var(--white); text-align: center; line-height: 1.08; }
</style>
</head>
<body>
<main class="canvas">
  <section class="card card-front" aria-label="Business card front">
    <div class="brand-row">
      <span class="brand-dot" aria-hidden="true"></span>
      <span class="brand-name">Colin Dartmoor<br>Constructions</span>
    </div>
    <div class="services">
      <ul>
        <li>Renovation</li>
        <li>Insurance Work</li>
      </ul>
      <ul>
        <li>Project Management</li>
        <li>All Forms Of Carpentry</li>
      </ul>
    </div>
    <div class="contact">
      <h1 class="person-name">Colin Dartmoor</h1>
      <p class="contact-line"><span class="label">M:</span>0461735920</p>
      <p class="contact-line"><span class="label">E:</span>colindartmoor@maildrop-example.com.au</p>
    </div>
    <div class="business-info">
      <p>POBox 728 Brenmoor 3971</p>
      <p><span class="label">ABN:</span>47 803 516 229</p>
    </div>
  </section>

  <section class="card card-back" aria-label="Business card back">
    <div class="back-mark">
      <span class="back-dot" aria-hidden="true"></span>
      <p class="back-name">Colin Dartmoor<br>Constructions</p>
    </div>
  </section>
</main>
</body>
</html>
```